Water ATM Card

Need a design for water ATM cards. Size of card is 3.375 x 2.125 inch
On the Front include the Cedar brook Logo.
Bottom right corner should have Price $100
On the Back
This card is to be used to access water refills at any Cedar Brook Water Vending Machines.
Please contact (869) 481 3927 or (869) 537 2914 or email clearflowtnx@examplemail.net for any assistance or recharging of card.

```html
<!DOCTYPE html>
<html lang="en">
<head>
<meta charset="utf-8">
<title>Cedar Brook Water ATM Card</title>
<link rel="stylesheet" href="https://fonts.googleapis.com/css2?family=Montserrat:wght@400;500;600;700;800&family=Oswald:wght@500;600&display=swap">
<style>
  :root {
    --sheet-grey: #939598;
    --ink: #111111;
    --white: #ffffff;
    --brand-blue: #1565b6;
    --banner-light: #1e7fcb;
    --banner-dark: #1c4fa0;
    --navy-band: #283a96;
    --water-light: #dbeaf6;
    --water-mid: #7fb1de;
    --water-deep: #2a63ad;
    --green-light: #7ec242;
    --green-dark: #1b9a4b;
    --back-top: #0c5a86;
    --back-bottom: #101a5c;
    --soft-text: #d6dde8;
  }
  * { box-sizing: border-box; margin: 0; padding: 0; }
  html, body { width: 1115px; height: 1200px; overflow: hidden; }
  body {
    background: var(--sheet-grey);
    font-family: "Montserrat", sans-serif;
    position: relative;
  }
  .side-label {
    position: absolute;
    left: 84px;
    font-size: 28px;
    font-weight: 500;
    color: var(--ink);
  }
  .side-label--front { top: 310px; }
  .side-label--back { top: 850px; }

  .card {
    position: absolute;
    left: 247px;
    width: 754px;
    height: 474px;
    overflow: hidden;
  }
  /* Front */
  .card--front { top: 93px; background: var(--white); }
  .title-banner {
    position: absolute;
    left: 93px; top: 34px;
    width: 568px; height: 65px;
    background: linear-gradient(180deg, var(--banner-light), var(--banner-dark));
    clip-path: polygon(0 0, 100% 0, 97% 50%, 100% 100%, 0 100%, 3% 50%);
    display: flex; align-items: center; justify-content: center;
    color: var(--white);
    font-size: 56px;
    font-weight: 400;
    letter-spacing: 0.5px;
    line-height: 1;
  }
  .title-banner strong { font-weight: 800; margin: 0 12px; }
  .water-splash {
    position: absolute;
    left: 0; right: 0; top: 170px; bottom: 18px;
    background:
      radial-gradient(ellipse at 20% 70%, rgba(42,99,173,0.55), transparent 60%),
      linear-gradient(180deg, rgba(255,255,255,0) 0%, var(--water-light) 35%, var(--water-mid) 75%, var(--water-deep) 100%);
  }
  .brand-name {
    position: absolute;
    left: 0; right: 0; top: 210px;
    text-align: center;
    font-size: 40px;
    font-weight: 800;
    color: var(--brand-blue);
    letter-spacing: 0.5px;
  }
  .brand-tagline {
    position: absolute;
    left: 0; right: 0; top: 248px;
    text-align: center;
    font-size: 24px;
    font-weight: 500;
    color: var(--brand-blue);
  }
  .price-tag { position: absolute; left: 570px; top: 250px; width: 170px; height: 200px; }
  .price-text {
    position: absolute;
    left: 570px; top: 336px; width: 162px;
    text-align: center;
    color: var(--white);
    line-height: 1;
  }
  .price-text .price-label { display: block; font-size: 21px; font-weight: 700; }
  .price-text .price-amount { display: block; font-family: "Oswald", sans-serif; font-size: 44px; font-weight: 600; margin-top: 2px; }
  .base-band {
    position: absolute;
    left: 0; right: 0; bottom: 0; height: 18px;
    background: var(--navy-band);
  }

  /* Back */
  .card--back {
    top: 633px;
    background: linear-gradient(135deg, var(--back-top), var(--back-bottom));
  }
  .stripe {
    position: absolute;
    left: 0; right: 0; top: 68px; height: 108px;
    background: linear-gradient(90deg, var(--green-light), var(--green-dark));
  }
  .signature-box {
    position: absolute;
    left: 50px; top: 224px;
    width: 99px; height: 84px;
    background: var(--white);
    border-radius: 13px;
  }
  .usage-note {
    position: absolute;
    left: 185px; top: 238px; width: 470px;
    font-size: 14px;
    line-height: 18.6px;
    color: var(--soft-text);
  }
  .contact-heading {
    position: absolute;
    left: 0; right: 0; top: 346px;
    display: flex; align-items: center; gap: 8px;
    color: var(--white);
    font-size: 21px;
    font-weight: 500;
  }
  .contact-heading::before, .contact-heading::after {
    content: "";
    flex: 1;
    height: 1.5px;
    background: var(--green-dark);
  }
  .contact-row {
    position: absolute;
    top: 380px;
    display: flex; align-items: center; gap: 8px;
    color: var(--white);
    font-size: 21px;
    white-space: nowrap;
  }
  .contact-row--phone { left: 27px; }
  .contact-row--email { left: 398px; top: 379px; font-size: 17px; gap: 6px; }
  .contact-icon { width: 34px; height: 34px; flex: none; }
  .assist-line {
    position: absolute;
    left: 0; right: 0; top: 420px;
    text-align: center;
    color: var(--white);
    font-size: 20px;
  }
</style>
</head>
<body>
  <div class="side-label side-label--front">Front</div>
  <div class="side-label side-label--back">Back</div>

  <section class="card card--front">
    <div class="title-banner">WATER<strong>ATM</strong>CARD</div>
    <div class="water-splash" role="img" aria-label="Photo of splashing clear blue water across the lower card"></div>
    <div class="brand-name">CEDAR BROOK</div>
    <div class="brand-tagline">Purified Spring Water</div>
    <svg class="price-tag" viewBox="0 0 170 200" aria-hidden="true">
      <defs>
        <linearGradient id="tagGreen" x1="0" y1="0" x2="1" y2="1">
          <stop offset="0" stop-color="#8cc63f"/>
          <stop offset="1" stop-color="#1b9a4b"/>
        </linearGradient>
      </defs>
      <path d="M84 0 C70 0 72 30 80 60 M84 0 C96 0 92 30 86 60" fill="none" stroke="#2b3f8f" stroke-width="2"/>
      <rect x="30" y="66" width="101" height="101" rx="8" transform="rotate(45 81 116)" fill="url(#tagGreen)"/>
      <circle cx="83" cy="47" r="4" fill="#ffffff" stroke="#2b3f8f" stroke-width="1.5"/>
    </svg>
    <div class="price-text">
      <span class="price-label">PRICE</span>
      <span class="price-amount">$100</span>
    </div>
    <div class="base-band"></div>
  </section>

  <section class="card card--back">
    <div class="stripe"></div>
    <div class="signature-box"></div>
    <p class="usage-note">Lorem ipsum dolor sit amet, consectetuer adipiscing elit, sed diam nonummy nibh euismod tincidunt ut laoreet dolore magna aliquam erat volutpat.</p>
    <div class="contact-heading">PLEASE CONTACT</div>
    <div class="contact-row contact-row--phone">
      <svg class="contact-icon" viewBox="0 0 34 34" aria-hidden="true">
        <rect x="7" y="7" width="20" height="20" rx="2" transform="rotate(45 17 17)" fill="#4caf50"/>
        <path d="M13 12 l2.5 -1 1.5 3 -1.5 1.2 c0.8 1.8 2 3 3.8 3.8 l1.2 -1.5 3 1.5 -1 2.5 c-5 0 -9.5 -4.5 -9.5 -9.5z" fill="#ffffff"/>
      </svg>
      <span>(869) 481 3927, (869) 537 2914</span>
    </div>
    <div class="contact-row contact-row--email">
      <svg class="contact-icon" viewBox="0 0 34 34" aria-hidden="true">
        <rect x="7" y="7" width="20" height="20" rx="2" transform="rotate(45 17 17)" fill="#4caf50"/>
        <rect x="11" y="13" width="12" height="8.5" fill="#ffffff"/>
        <path d="M11 13 l6 5 6 -5" fill="none" stroke="#4caf50" stroke-width="1.2"/>
      </svg>
      <span>clearflowtnx@examplemail.net</span>
    </div>
    <div class="assist-line">For any Assistance or Recharging of Card</div>
  </section>
</body>
</html>
```